Theme design for Voltwick Showcase in Miami South Beach

We are holding the Voltwick Showcase in South Beach Miami and want some theme design that we can use on all templates materials.

https://www.plenvora.com/design/QXRMbnTe8Lk/5HwYpaQcZrEjvDnMuKsLfo/view?utm_content=QXRMbnTe8Lk&utm_campaign=designshare&utm_medium=link&utm_source=editor

Target Market(s)

Cell Phone & Gadget Repair

Industry/Entity Type

Electronics repair

Requirements
Must have
• Miami Theme
Nice to have
• Miami based theme

```html
<!DOCTYPE html>
<html lang="en">
<head>
<meta charset="utf-8">
<title>Voltwick Showcase in Miami – Theme Board</title>
<link href="https://fonts.googleapis.com/css2?family=Lobster&family=Montserrat:wght@400;800;900&display=swap" rel="stylesheet">
<style>
  :root {
    --board-top: #d98be0;
    --board-bottom: #f4b08e;
    --label-grey: #8c8a8c;
    --brand-blue: #1479c9;
    --sky-blue: #1a96dd;
    --sand: #d39a64;
    --sand-band: #c8976a;
    --navy: #1b2140;
    --white: #ffffff;
    --pill-blue: #a9c9ee;
    --photo-light: #b9b6b8;
    --photo-dark: #4a4a50;
  }
  * { box-sizing: border-box; margin: 0; padding: 0; }
  html, body { width: 870px; height: 1200px; overflow: hidden; }
  body {
    position: relative;
    background: linear-gradient(180deg, var(--board-top) 0%, #e7a3c8 55%, var(--board-bottom) 100%);
    font-family: "Montserrat", sans-serif;
    color: var(--navy);
  }
  .abs { position: absolute; }

  /* Board labels */
  .board-label {
    position: absolute;
    font-weight: 900;
    color: var(--label-grey);
    letter-spacing: 1px;
    white-space: nowrap;
  }
  .board-label--flyer {
    font-size: 25px;
    left: 676px; top: 400px;
    transform: translate(-50%, -50%) rotate(-90deg);
  }
  .board-label--cover {
    font-size: 25px;
    left: 430px; top: 1162px;
    transform: translate(-50%, -50%);
  }

  /* Shared pieces */
  .brand-name {
    position: absolute;
    display: flex; align-items: center; gap: 10px;
    font-weight: 900;
    color: var(--brand-blue);
    text-transform: uppercase;
    white-space: nowrap;
  }
  .brand-name .brand-square { background: var(--brand-blue); border-radius: 6px; flex: none; }
  .script-title { position: absolute; font-family: "Lobster", cursive; white-space: nowrap; line-height: 1; }
  .script-title .in {
    color: var(--sky-blue);
    -webkit-text-stroke: 4px var(--white); paint-order: stroke fill;
    text-shadow: 3px 4px 0 rgba(80,60,120,.35);
  }
  .script-title .city {
    color: var(--sand);
    -webkit-text-stroke: 6px var(--white); paint-order: stroke fill;
    text-shadow: 4px 5px 0 rgba(80,60,120,.35);
  }
  .photo-slot {
    position: absolute;
    background: linear-gradient(150deg, var(--photo-light) 0%, #8e8c92 45%, var(--photo-dark) 100%);
    border: 5px solid var(--white);
    overflow: hidden;
  }
  .presenter-name {
    position: absolute; color: var(--white); font-weight: 900; white-space: nowrap;
    letter-spacing: .3px;
  }
  .partner-badge {
    position: absolute; border-radius: 50%;
    background: var(--white);
    box-shadow: 0 3px 8px rgba(0,0,0,.18);
    display: flex; align-items: center; justify-content: center; text-align: center;
    font-weight: 900; color: var(--navy); line-height: 1.05; text-transform: uppercase;
  }
  .heading { position: absolute; font-weight: 900; white-space: nowrap; text-transform: uppercase; }
  .body-copy { position: absolute; font-weight: 400; white-space: nowrap; }

  /* Flyer */
  .flyer {
    position: absolute; left: 43px; top: 31px; width: 552px; height: 748px;
    background: linear-gradient(180deg, #ebe5e3 0%, #f7d2d4 30%, #fbbec4 52%, #fd9e8a 75%, #ff6b2c 100%);
    box-shadow: 0 6px 14px rgba(60,20,60,.35);
    overflow: hidden;
  }
  .flyer .tagline-band {
    left: 110px; top: 294px; width: 350px; height: 48px;
    background: var(--sand-band);
    border-radius: 4px 22px 6px 18px;
    transform: rotate(-1deg);
    display: flex; align-items: center; justify-content: center;
    color: var(--white); font-weight: 900; font-size: 33px;
  }
  .flyer .photo-slot {
    left: -5px; top: 374px; width: 340px; height: 272px;
    border-radius: 0 120px 0 0;
  }
  .venue-pill {
    position: absolute; background: var(--sand-band); border-radius: 8px;
    display: flex; align-items: center; justify-content: center;
    font-weight: 900; color: var(--navy); white-space: nowrap;
    box-shadow: 0 3px 5px rgba(0,0,0,.2);
  }

  /* Cover */
  .cover {
    position: absolute; left: 42px; top: 809px; width: 775px; height: 315px;
    background: linear-gradient(160deg, #ecdfe3 0%, #f6c8cc 45%, #fbb4a2 75%, #ff8a55 100%);
    box-shadow: 0 6px 14px rgba(60,20,60,.35);
    overflow: hidden;
  }
  .cover .photo-slot {
    left: 470px; top: -5px; width: 253px; height: 290px;
    border-radius: 0 0 95px 0;
  }
  .date-pill {
    position: absolute; background: var(--pill-blue); border-radius: 8px;
    display: flex; align-items: center; justify-content: center;
    font-weight: 900; color: var(--navy); white-space: nowrap;
  }
</style>
</head>
<body>

  <!-- Flyer and social media post -->
  <section class="flyer">
    <div class="brand-name" style="left:118px; top:62px; font-size:34px; line-height:1.05;">
      <span class="brand-square" style="width:40px; height:40px;"></span>
      <span>Voltwick<br>Showcase</span>
    </div>

    <div class="script-title" style="left:66px; top:180px;">
      <span class="in" style="font-size:68px;">In</span>
      <span class="city" style="font-size:112px;">Miami</span>
    </div>

    <div class="abs tagline-band">YOUR TEXT</div>

    <div class="photo-slot" role="img" aria-label="Photo of the presenter at his repair bench holding a phone screen in front of a laminating machine">
      <span class="presenter-name" style="left:38px; bottom:12px; font-size:14px;">RAFAEL ORTEGA</span>
    </div>
    <div class="partner-badge" style="left:236px; top:565px; width:88px; height:88px; font-size:12px;">Handset<br>Clinic</div>

    <div class="heading" style="right:29px; top:408px; font-size:18px; color:var(--navy);">Find me booth 46</div>
    <div class="body-copy" style="right:29px; top:436px; font-size:12px; text-align:right; line-height:19px;">live demos both days and<br>many more</div>

    <div class="heading" style="right:29px; top:500px; font-size:18px; color:var(--sky-blue); text-align:right; line-height:24px;">Learn how to<br>refurb LCS'D</div>

    <div class="heading" style="right:24px; top:583px; font-size:19px; color:var(--navy); text-align:right; line-height:25px;">7th and 8th<br>November 2025</div>

    <div class="venue-pill" style="left:80px; top:687px; width:392px; height:32px; font-size:16px;">BAYFRONT CONVENTION HALL</div>
  </section>

  <div class="board-label board-label--flyer">FLYER AND SOCIAL MEDIA POST</div>

  <!-- Cover and website hero -->
  <section class="cover">
    <div class="brand-name" style="left:78px; top:24px; font-size:26px; line-height:1.05;">
      <span class="brand-square" style="width:32px; height:32px;"></span>
      <span>Voltwick<br>Showcase</span>
    </div>

    <div class="script-title" style="left:76px; top:118px;">
      <span class="in" style="font-size:38px;">In</span>
      <span class="city" style="font-size:64px;">Miami</span>
    </div>

    <div class="heading" style="left:203px; top:195px; width:0; font-size:16px; color:var(--navy);"><span style="position:absolute; transform:translateX(-50%);">Find me booth 46</span></div>
    <div class="body-copy" style="left:140px; top:218px; font-size:10px;">live demos both days and</div>
    <div class="date-pill" style="left:112px; top:238px; width:170px; height:15px; font-size:8.5px;">7TH AND 8TH NOVEMBER 2025</div>
    <div class="heading" style="left:40px; top:271px; font-size:16px; color:var(--navy);">Bayfront Convention Hall</div>

    <div class="photo-slot" role="img" aria-label="Photo of the presenter at his repair bench holding a phone screen in front of a laminating machine">
      <span class="presenter-name" style="left:110px; bottom:12px; font-size:11px;">RAFAEL ORTEGA</span>
    </div>
    <div class="partner-badge" style="left:444px; top:206px; width:90px; height:90px; font-size:12px;">Handset<br>Clinic</div>
  </section>

  <div class="board-label board-label--cover">COVER AND WEBSITE HERO</div>

</body>
</html>
```